Post Card (5x7) - Pre-foreclosure Image - Harbor Path Partners

(Two-Sided Post Card)
FACING FORECLOSURE? YOU STILL HAVE OPTIONS.
If you’re behind on payments or at risk of foreclosure, you’re not alone—and it’s not too late to take action.
We help homeowners:
• Explore options to stay in their home
• Stop or delay foreclosure
• Sell quickly for a fair price if needed
No pressure. No obligation. Just real solutions tailored to your situation.
Call - (240) 558-2094
Email - marcus@hpbllc-mail.com
Harbor Path Partners LLC
7200 Bramwick Lane, Ellicott City, MD 21043
**Marcus Fennimore is a Licensed Realtor with Copperleaf Homes Realty in Bethesda, Maryland.
(Leave room for mailing address, return address & postage)
Target Market(s)
Distressed Homeowners
Industry/Entity Type
Real Estate

```html
<!DOCTYPE html>
<html lang="en">
<head>
<meta charset="utf-8">
<title>Harbor Path Partners – Pre-foreclosure Post Card</title>
<link href="https://fonts.googleapis.com/css2?family=Poppins:wght@400;500;600;700;800&display=swap" rel="stylesheet">
<style>
  :root {
    --navy: #0b1622;
    --orange: #f28e2b;
    --white: #ffffff;
    --ink: #2b2f36;
    --backdrop: #e6e7e9;
    --sun-1: #f7b23a;
    --sun-2: #c9761f;
    --sun-3: #3a2a1c;
  }
  * { margin: 0; padding: 0; box-sizing: border-box; }
  html, body { width: 942px; height: 1200px; overflow: hidden; }
  body { background: var(--backdrop); font-family: "Poppins", sans-serif; position: relative; }

  .card { position: absolute; left: 129px; width: 684px; height: 459px; overflow: hidden; }
  .card--front { top: 121px; background: var(--navy); color: var(--white); }
  .card--back { top: 619px; background: var(--white); }
  .layer { position: absolute; inset: 0; }
  .abs { position: absolute; }

  .brand { position: absolute; width: 200px; text-align: center; }
  .brand-main { font-weight: 500; font-size: 16px; letter-spacing: 3px; line-height: 18px; white-space: nowrap; }
  .brand-sub { display: flex; align-items: center; justify-content: center; gap: 7px; font-weight: 500; font-size: 8.5px; letter-spacing: 3px; line-height: 12px; white-space: nowrap; }
  .brand-sub::before, .brand-sub::after { content: ""; width: 34px; height: 1.2px; background: currentColor; }
  .brand--light { color: var(--white); }
  .brand--dark { color: var(--navy); }

  .headline { left: 50px; top: 122px; font-weight: 800; font-size: 38px; line-height: 36px; }
  .headline .accent { color: var(--orange); display: block; }
  .subhead { left: 51px; top: 205px; font-weight: 600; font-size: 17.5px; }
  .subhead span { color: var(--orange); }
  .rule { left: 50px; top: 233px; width: 40px; height: 3px; background: var(--orange); }
  .intro { left: 50px; top: 241px; width: 270px; font-size: 11.3px; line-height: 13.6px; }
  .intro strong { color: var(--orange); font-weight: 600; }

  .benefit { top: 302px; width: 110px; text-align: center; }
  .benefit svg { display: block; margin: 0 auto 6px; }
  .benefit-title { color: var(--orange); font-weight: 700; font-size: 8.2px; line-height: 10px; }
  .benefit-text { font-size: 8px; line-height: 9px; }
  .divider { top: 302px; width: 1px; height: 80px; background: var(--white); }

  .promise { left: 95px; top: 410px; color: var(--navy); }
  .promise-title { font-weight: 700; font-size: 12.4px; line-height: 15px; }
  .promise-text { font-size: 11.8px; line-height: 14px; }

  .contact { left: 34px; width: 180px; height: 34px; }
  .contact-icon { position: absolute; left: 0; top: 0; width: 34px; height: 34px; border-radius: 50%; background: var(--navy); }
  .contact-label { position: absolute; left: 43px; color: var(--orange); font-weight: 600; font-size: 8px; letter-spacing: .2px; white-space: nowrap; }
  .contact-value { position: absolute; left: 43px; color: var(--navy); font-size: 10px; line-height: 13px; white-space: nowrap; }
  .contact-value--phone { font-weight: 700; font-size: 13.5px; line-height: 16px; }
  .contact-rule { left: 34px; width: 160px; height: 1px; background: #d7d9dc; }

  .disclosure { left: 98px; top: 393px; color: var(--white); font-size: 9.6px; line-height: 12.8px; width: 200px; }
  .disclosure strong { font-weight: 600; }

  .mail-label { color: var(--ink); font-size: 10.3px; letter-spacing: .3px; }
  .postage { left: 576px; top: 35px; width: 74px; height: 77px; border: 1px solid var(--ink); display: flex; align-items: center; justify-content: center; text-align: center; font-size: 10px; line-height: 15.5px; color: var(--ink); }
  .address-line { left: 394px; width: 256px; height: 1px; background: var(--ink); }
</style>
</head>
<body>

<!-- FRONT -->
<section class="card card--front">
  <svg class="layer" width="684" height="459" viewBox="0 0 684 459">
    <defs>
      <linearGradient id="sunset" x1="0" y1="0" x2="0" y2="1">
        <stop offset="0" stop-color="#4d4a4a"/>
        <stop offset=".3" stop-color="#b5762c"/>
        <stop offset=".45" stop-color="var(--sun-1)"/>
        <stop offset=".62" stop-color="var(--sun-3)"/>
        <stop offset=".8" stop-color="var(--sun-2)"/>
        <stop offset="1" stop-color="#2a1e14"/>
      </linearGradient>
    </defs>
    <polygon points="286,0 684,0 684,459 522,459" fill="url(#sunset)" role="img" aria-label="Photo of a city skyline silhouetted at sunset over a river"/>
    <polygon points="0,392 432,392 401,459 0,459" fill="var(--orange)"/>
  </svg>

  <div class="brand brand--light" style="left:37px;top:78px;">
    <div class="brand-main">HARBOR PATH</div>
    <div class="brand-sub">PARTNERS LLC</div>
  </div>

  <h1 class="abs headline">FACING<span class="accent">FORECLOSURE?</span></h1>
  <p class="abs subhead">YOU STILL HAVE <span>OPTIONS.</span></p>
  <div class="abs rule"></div>
  <p class="abs intro">If you’re behind on payments or at risk of foreclosure, you’re not alone—and <strong>it’s not too late to take action.</strong></p>

  <div class="abs benefit" style="left:34px;">
    <svg width="44" height="44" viewBox="0 0 44 44" fill="none" stroke="#fff" stroke-width="1.3">
      <circle cx="22" cy="22" r="20.5"/>
      <path d="M12 22 L22 13 L32 22 M15 20 V31 H29 V20 M20 31 V25 H24 V31"/>
    </svg>
    <div class="benefit-title">EXPLORE OPTIONS</div>
    <div class="benefit-text">to stay in<br>your home</div>
  </div>
  <div class="abs divider" style="left:147px;"></div>
  <div class="abs benefit" style="left:150px;">
    <svg width="44" height="44" viewBox="0 0 44 44" fill="none" stroke="#fff" stroke-width="1.3">
      <circle cx="22" cy="22" r="20.5"/>
      <circle cx="19" cy="20" r="7"/>
      <path d="M19 16 V20 L22 22"/>
      <path d="M26 22 L32 32 H20 Z" fill="#fff"/>
    </svg>
    <div class="benefit-title">STOP OR DELAY</div>
    <div class="benefit-text">foreclosure</div>
  </div>
  <div class="abs divider" style="left:263px;"></div>
  <div class="abs benefit" style="left:265px;">
    <svg width="44" height="44" viewBox="0 0 44 44" fill="none" stroke="#fff" stroke-width="1.3">
      <circle cx="22" cy="22" r="20.5"/>
      <path d="M10 20 L16 17 L22 20 L28 17 L34 20 M14 24 L19 28 L22 26 L25 28 L30 24 M22 8 V12 M16 10 L18 13 M28 10 L26 13"/>
    </svg>
    <div class="benefit-title">SELL QUICKLY</div>
    <div class="benefit-text">for a fair price<br>if needed</div>
  </div>

  <svg class="abs" style="left:50px;top:410px;" width="31" height="33" viewBox="0 0 31 33" fill="none" stroke="var(--navy)" stroke-width="2.6" stroke-linejoin="round">
    <path d="M15.5 2 L28.5 6 V15 C28.5 23 22 28.5 15.5 31 C9 28.5 2.5 23 2.5 15 V6 Z"/>
    <path d="M9.5 16 L14 20.5 L22 12"/>
  </svg>
  <div class="abs promise">
    <div class="promise-title">No pressure. No obligation.</div>
    <div class="promise-text">Just real solutions tailored to your situation.</div>
  </div>
</section>

<!-- BACK -->
<section class="card card--back">
  <svg class="layer" width="684" height="459" viewBox="0 0 684 459">
    <defs>
      <linearGradient id="skyline" x1="0" y1="0" x2="0" y2="1">
        <stop offset="0" stop-color="#5b5450"/>
        <stop offset=".35" stop-color="#a86c2c"/>
        <stop offset=".6" stop-color="#3d2c1f"/>
        <stop offset="1" stop-color="#1c1712"/>
      </linearGradient>
    </defs>
    <polygon points="258,0 342,0 342,357 255,357 196,189" fill="var(--navy)"/>
    <polygon points="263,0 342,0 342,357 261,357 202,189" fill="url(#skyline)" role="img" aria-label="Photo of city towers silhouetted against a sunset sky"/>
    <rect x="0" y="357" width="342" height="102" fill="var(--navy)"/>
  </svg>

  <div class="brand brand--dark" style="left:18px;top:75px;">
    <div class="brand-main">HARBOR PATH</div>
    <div class="brand-sub">PARTNERS LLC</div>
  </div>

  <div class="abs contact" style="top:160px;">
    <div class="contact-icon">
      <svg width="34" height="34" viewBox="0 0 34 34" fill="none" stroke="#fff" stroke-width="1.4"><rect x="13" y="9" width="8" height="16" rx="1.5"/><circle cx="17" cy="22.5" r=".6" fill="#fff"/></svg>
    </div>
    <div class="contact-label" style="top:1px;">CALL</div>
    <div class="contact-value contact-value--phone" style="top:13px;">(240) 558-2094</div>
  </div>
  <div class="abs contact-rule" style="top:204px;"></div>
  <div class="abs contact" style="top:217px;">
    <div class="contact-icon">
      <svg width="34" height="34" viewBox="0 0 34 34" fill="#fff"><path d="M9 11 H25 V23 H9 Z"/><path d="M9 11 L17 18 L25 11" fill="none" stroke="var(--navy)" stroke-width="1.3"/></svg>
    </div>
    <div class="contact-label" style="top:2px;">EMAIL</div>
    <div class="contact-value" style="top:15px;">marcus@hpbllc-mail.com</div>
  </div>
  <div class="abs contact-rule" style="top:260px;"></div>
  <div class="abs contact" style="top:270px;">
    <div class="contact-icon">
      <svg width="34" height="34" viewBox="0 0 34 34"><path d="M17 8 C12.5 8 10 11 10 14.5 C10 19 17 26 17 26 C17 26 24 19 24 14.5 C24 11 21.5 8 17 8 Z" fill="#fff"/><circle cx="17" cy="14.5" r="2.8" fill="var(--navy)"/></svg>
    </div>
    <div class="contact-label" style="top:0;">HARBOR PATH PARTNERS LLC</div>
    <div class="contact-value" style="top:13px;">7200 Bramwick Lane,<br>Ellicott City, MD 21043</div>
  </div>

  <div class="abs brand--light" style="left:20px;top:392px;width:66px;text-align:center;font-weight:500;font-size:8.5px;letter-spacing:1.4px;line-height:12px;">HARBOR<br>PATH<br>PARTNERS</div>
  <p class="abs disclosure"><strong>Marcus Fennimore</strong> is a Licensed Realtor with Copperleaf Homes Realty in Bethesda, Maryland.</p>

  <div class="abs" style="left:357px;top:33px;width:1px;height:393px;background:var(--ink);"></div>
  <div class="abs mail-label" style="left:394px;top:45px;">RETURN ADDRESS</div>
  <div class="abs postage">PLACE<br>POSTAGE<br>HERE</div>
  <div class="abs mail-label" style="left:394px;top:271px;font-size:12.5px;">DELIVER TO:</div>
  <div class="abs address-line" style="top:314px;"></div>
  <div class="abs address-line" style="top:350px;"></div>
  <div class="abs address-line" style="top:386px;"></div>
  <div class="abs address-line" style="top:422px;"></div>
</section>

</body>
</html>
```